'Cradle Ahead' promotional brochure

We have designed a 6 week program to educate impending first-time parents about the things they need to know to survive the first 6 months. Sessions delivered by general practitioner/family doctor, dietician, physiotherapist, speech pathologist and psychologist. Our promotional blurb is: 'A comprehensive education program for first-time parents-to-be, delivered over 6 weeks by health professionals in your community, about everything you need to know to look after your baby (and yourself!) in the first 6 months'. I now want to put together a promotional brochure to be distributed to those couples who express an interest which will provide further details of what will be delivered in the course.
Updates
In terms of layout, I envisaged a double sided A4 size, foldable into 3 sections, but very happy to be guided on this.
Target Market(s)
To appeal to a young, well educated demographic. First time parents couples.
Industry/Entity Type
Medical
Font styles to use
Other font styles liked:
- Playfair Display
Requirements
Must have
- Playfair display font to be consistent with our logo (attached). Logo also included please. Some consistency with colours of logo please.
Nice to have
- I am a doctor, and have no creative genes! But prefer a clean and professional appearance overall. Not too cluttered in overall appearance.
Should not have
- No cheesy pictures of babies.

```html
<!DOCTYPE html>
<html lang="en">
<head>
<meta charset="utf-8">
<title>Cradle Ahead – Brochure</title>
<link rel="stylesheet" href="https://fonts.googleapis.com/css2?family=Playfair+Display:wght@400;700;900&display=swap">
<style>
:root{
  --green:#5aa832;
  --green-dark:#3f8f24;
  --lime:#8cc63f;
  --lime-soft:#9fd24e;
  --grey-ring:#707070;
  --white:#ffffff;
  --stage:#dedede;
  --serif:'Playfair Display', Georgia, serif;
}
*{box-sizing:border-box;margin:0;padding:0}
html,body{width:1200px;height:1000px;overflow:hidden}
body{background:var(--stage);font-family:var(--serif);position:relative}
.sheet{position:absolute;left:270px;width:660px;height:467px;box-shadow:0 4px 14px rgba(0,0,0,.18);overflow:hidden}
.sheet--outside{top:22px}
.sheet--inside{top:510px}
.panel{position:absolute;top:0;width:220px;height:467px;overflow:hidden}
.panel--left{left:0}
.panel--middle{left:220px}
.panel--right{left:440px}
.panel + .panel{border-left:1px solid rgba(0,0,0,.06)}
.panel svg.shapes{position:absolute;left:0;top:0}
.abs{position:absolute}

/* outside – left */
.tagline{left:18px;top:16px;width:105px;color:var(--lime);font-weight:700;font-size:17px;line-height:1.12;text-transform:uppercase}
.blurb{left:22px;top:252px;width:182px;color:var(--lime);font-size:11px;line-height:1.55;text-transform:uppercase;text-align:center}

/* outside – middle */
.join{left:40px;top:30px;width:140px;text-align:center;color:var(--green);text-transform:uppercase}
.join__title{font-weight:700;font-size:16px;line-height:1.15}
.join__sub{font-weight:700;font-size:9.5px;margin-top:5px;line-height:1.3}
.join__rule{border-top:1px dashed var(--green);width:90px;margin:6px auto}
.join__phone{font-weight:700;font-size:11px}

/* outside – right */
.brand{left:96px;top:22px;width:112px;display:flex;align-items:center;gap:5px;color:var(--green);font-size:9px;line-height:1.15;text-transform:uppercase}
.brand__mark{width:12px;height:12px;border-radius:50%;background:var(--green);flex:none}
.title{left:10px;top:138px;width:205px;text-align:center;color:var(--white);font-weight:900;font-size:34px;line-height:1.05;text-transform:uppercase}
.cost{left:150px;top:240px;width:66px;text-align:center;color:var(--white);font-weight:700;text-transform:uppercase}
.cost__label{font-size:8px}
.cost__price{font-size:17px}
.promo{left:18px;top:306px;width:192px;text-align:center;color:var(--green);font-weight:900;text-transform:uppercase;line-height:1.02;font-size:12px}
.promo b{font-size:18px;font-weight:900}

/* inside */
.week{color:var(--white);font-size:7.2px;line-height:1.35}
.week h2{font-size:13px;font-weight:700;text-transform:uppercase;text-decoration:underline;text-underline-offset:2px;margin-bottom:4px}
.week p{margin-bottom:6px;text-align:justify}
.week ul{list-style:none;margin-bottom:6px}
.week li::before{content:". "}
.feature{left:40px;top:278px;width:140px;text-align:center;color:var(--green);font-weight:700;text-transform:uppercase;font-size:11.5px;line-height:1.08}
.feature b{font-size:20px}
</style>
</head>
<body>

<section class="sheet sheet--outside">
  <div class="panel panel--left">
    <svg class="shapes" width="220" height="467" viewBox="0 0 220 467">
      <rect width="220" height="467" fill="var(--green)"/>
      <path d="M0 120 Q110 150 220 118 L220 300 L0 300Z" fill="var(--lime)"/>
      <circle cx="45" cy="35" r="125" fill="var(--white)"/>
      <circle cx="150" cy="385" r="205" fill="var(--green-dark)"/>
      <circle cx="150" cy="390" r="196" fill="var(--white)"/>
    </svg>
    <div class="abs tagline">Best baby care for 6 first months</div>
    <div class="abs blurb">A comprehensive education program for first-time parents-to-be, delivered over 6 weeks by health professionals in your community, about everything you need to know to look after your baby (and yourself!) in the first 6 months</div>
  </div>

  <div class="panel panel--middle">
    <svg class="shapes" width="220" height="467" viewBox="0 0 220 467">
      <defs>
        <radialGradient id="familyTones" cx="50%" cy="55%" r="70%">
          <stop offset="0" stop-color="#f6e3d6"/>
          <stop offset=".6" stop-color="#e9cdb9"/>
          <stop offset="1" stop-color="#f4efea"/>
        </radialGradient>
      </defs>
      <rect width="220" height="467" fill="url(#familyTones)" role="img" aria-label="Photo of parents smiling at their baby holding a yellow flower"/>
      <path d="M0 0 Q-5 250 30 467 L0 467Z" fill="var(--green)"/>
      <path d="M220 0 Q215 250 195 467 L220 467Z" fill="var(--green)"/>
      <circle cx="110" cy="78" r="104" fill="var(--green)"/>
      <circle cx="110" cy="78" r="92" fill="var(--white)"/>
      <circle cx="110" cy="475" r="55" fill="var(--white)" stroke="var(--grey-ring)" stroke-width="14"/>
    </svg>
    <div class="abs join">
      <div class="join__title">Join us whoever you are.</div>
      <div class="join__sub">Contact details for enquiries/bookings</div>
      <div class="join__rule"></div>
      <div class="join__phone">(02) 5550 1234</div>
    </div>
  </div>

  <div class="panel panel--right">
    <svg class="shapes" width="220" height="467" viewBox="0 0 220 467">
      <rect width="220" height="467" fill="var(--green)"/>
      <circle cx="155" cy="40" r="72" fill="var(--white)"/>
      <circle cx="200" cy="420" r="200" fill="var(--lime)"/>
      <circle cx="160" cy="470" r="200" fill="var(--white)"/>
      <circle cx="183" cy="260" r="40" fill="var(--green)" stroke="var(--grey-ring)" stroke-width="8"/>
      <rect x="120" y="252" width="22" height="8" rx="2" fill="var(--white)"/>
    </svg>
    <div class="abs brand"><span class="brand__mark"></span><span>Banksia Health &amp; Medical</span></div>
    <h1 class="abs title">Cradle Ahead</h1>
    <div class="abs cost"><div class="cost__label">Total cost</div><div class="cost__price">$300</div></div>
    <div class="abs promo">A comprehensive education program for <b>first-time</b> parents-to-be about everything you need to know to look after <b>your baby</b> (and yourself!) in <b>the first 6 months</b></div>
  </div>
</section>

<section class="sheet sheet--inside">
  <div class="panel panel--left">
    <svg class="shapes" width="220" height="467" viewBox="0 0 220 467">
      <defs>
        <linearGradient id="motherTones" x1="0" y1="0" x2="1" y2="1">
          <stop offset="0" stop-color="#8a6a55"/>
          <stop offset=".5" stop-color="#c9a58c"/>
          <stop offset="1" stop-color="#6c5a66"/>
        </linearGradient>
      </defs>
      <rect width="220" height="467" fill="var(--lime)"/>
      <path d="M0 0 L205 0 Q190 110 0 145Z" fill="var(--white)"/>
      <path d="M0 0 L198 0 Q182 102 0 135Z" fill="url(#motherTones)" role="img" aria-label="Photo of a mother cuddling her newborn"/>
      <circle cx="30" cy="470" r="45" fill="none" stroke="var(--green)" stroke-width="8"/>
    </svg>
    <div class="abs week" style="left:18px;top:155px;width:190px">
      <h2>Week 1</h2>
      <p>GP Dr Anna Whitfield will share information for Mum's own health after delivery. Topics include:</p>
      <ul>
        <li>Vaccinations in pregnancy</li>
        <li>Bleeding, bladder and bowel after delivery</li>
        <li>Breastfeeding, engorgement and mastitis</li>
        <li>Bottle feeding</li>
        <li>Post-natal anxiety &amp; depression</li>
        <li>Intimacy and contraception</li>
      </ul>
      <h2 style="margin-top:8px">Week 2</h2>
      <p>Session 1 - Clinical Psychologist Dr Mara Lindqvist will discuss changes in relationships as couples become parents, gender roles in parenting and post-natal depression.</p>
      <p>Session 2 - Physiotherapist Tess Morrow will present advice for Mums regarding exercise during and after pregnancy, looking after the pelvic floor during and after pregnancy, and abdominal muscle separation management. She will also provide advice for promoting babies' neck strength and minimising the risk of flat spots on the head and encouraging gross motor skills in the first 6 months.</p>
    </div>
  </div>

  <div class="panel panel--middle">
    <svg class="shapes" width="220" height="467" viewBox="0 0 220 467">
      <rect width="220" height="467" fill="var(--lime-soft)"/>
      <circle cx="110" cy="340" r="102" fill="var(--green)"/>
      <circle cx="110" cy="340" r="90" fill="var(--white)"/>
    </svg>
    <div class="abs week" style="left:16px;top:20px;width:190px">
      <h2>Week 3</h2>
      <p>Session 1 - Dietician Ruth Calder provides advice for Mums regarding healthy eating during pregnancy and lactation, normal weight gain during pregnancy and realistic weight loss after. She will also discuss the evidence regarding breastfeeding VS bottle-feeding, normal infant weight gain and introducing solids (including those with potential for allergy).</p>
      <p>Session 2 - Paediatric Speech Pathologist Nell Carver will share information about latching and breast-feeding troubles &amp; tongue tie, advice about dummies and finger-sucking, introducing solids &amp; feeding (including 'pouch' food), encouraging language development and current evidence about electronic devices impacting language development.</p>
    </div>
    <div class="abs feature"><b>6</b> weeks of comprehensive parent education program for baby health care for the first 6 months</div>
  </div>

  <div class="panel panel--right">
    <svg class="shapes" width="220" height="467" viewBox="0 0 220 467">
      <defs>
        <linearGradient id="babyTones" x1="0" y1="0" x2="1" y2="1">
          <stop offset="0" stop-color="#dfe9f2"/>
          <stop offset=".5" stop-color="#f1d9c4"/>
          <stop offset="1" stop-color="#9fb9d6"/>
        </linearGradient>
      </defs>
      <rect width="220" height="467" fill="var(--lime)"/>
      <circle cx="175" cy="40" r="60" fill="none" stroke="var(--green)" stroke-width="8"/>
      <path d="M220 467 L30 467 Q60 370 220 360Z" fill="var(--white)"/>
      <path d="M220 467 L40 467 Q70 378 220 370Z" fill="url(#babyTones)" role="img" aria-label="Photo of a baby in a knitted hat lying beside a toy car"/>
    </svg>
    <div class="abs week" style="left:16px;top:22px;width:190px">
      <h2>Week 4</h2>
      <p style="margin-bottom:2px">GP Dr Anna Whitfield will share advice about your babies' health in the first 6 months, including:</p>
      <ul>
        <li>Skin of newborns</li>
        <li>Sleeping</li>
        <li>Crying</li>
        <li>Immunisations</li>
        <li>Fever and infections</li>
        <li>Diarrhoea and constipation</li>
        <li>Teething</li>
        <li>Understanding a baby's signals</li>
      </ul>
      <h2>Week 5</h2>
      <p>Clinical Psychologist Dr Mara Lindqvist will share information about bonding &amp; attachment with your baby, how to promote their social &amp; emotional development and how to manage separation anxiety. She will also discuss positive parenting approaches.</p>
      <h2>Week 6</h2>
      <p>Session 1 - Secret Men's Business – a men-only session (including beer!) with a new father for frank discussion about the road ahead. Mums will do a shopping excursion with the GP &amp; Dietician to Greenway Market to look at baby products and food - the good and the bad!</p>
      <p>Session 2 - Program review, reflection and evaluation and future session planning when baby is 6 months of age.</p>
    </div>
  </div>
</section>

</body>
</html>
```